Titlescreen rework for real estate homepage

Hello, this is my homepage (http://www.wolde-immobilien.de) and I am just looking for a title page for the title screen. So I guess the main target is finding a fitting picture for it. Re-arranging the menu is not a must, but I at the open everything even for new Ideas of additional elements. The rest of the homepage stays as it is. What I'm looking for is taff to describe, I already needed a long time finding the current picture. I am a real estate agent so it should have a link to estates. It could be a dark theme as it now or maybe something more light with "white" in it as you can scroll down. Of course it should work with the elements appearing bottom. Because I do not work in New York, just in a smaller area in Germany, no scyscrappers to find. I hope someone can show up with a new and fitting new title screen for me. I uploaded the logo-file for you to build in. The used font is raleway, cause its used in the logo as well. Its downloadable here: (https://www.typeorchard.com/fonts/raleway)
Target Market(s)
Real-Estate
Industry/Entity Type
Real Estate
Number of Pages Required
1 page
Look and feel

```html
<!DOCTYPE html>
<html lang="de">
<head>
<meta charset="utf-8">
<title>Wolde Immobilien</title>
<link rel="stylesheet" href="https://fonts.googleapis.com/css2?family=Raleway:wght@300;400;500;600;700;800&display=swap">
<style>
:root{
  --black:#000;
  --ink:#111;
  --dark:#1a1a1a;
  --white:#fff;
  --grey-text:#555;
  --light-text:#cfcfcf;
  --line:#d0d0d0;
  --btn:#5a5a5a;
  --accent:#2c3e50;
}
*{margin:0;padding:0;box-sizing:border-box}
html,body{width:1200px;height:3064px;overflow:hidden}
body{font-family:'Raleway',sans-serif;background:var(--white);color:var(--ink);position:relative}
section,header,footer{position:absolute;left:0;width:1200px}
.photo{position:absolute}

/* hero */
.hero{top:0;height:540px;background:var(--black)}
.hero .photo{inset:0;background:linear-gradient(135deg,#3a342e 0%,#241f1b 40%,#4a4640 70%,#1c1a18 100%)}
.nav{position:absolute;top:0;left:0;width:1200px;height:80px;display:flex;align-items:center;justify-content:space-between;padding:0 40px}
.brand{display:flex;align-items:center;gap:10px;color:var(--white);font-weight:700;font-size:18px}
.brand-mark{width:14px;height:14px;background:var(--white)}
.menu{display:flex;gap:18px;list-style:none;color:var(--white);font-size:13px;font-weight:500}
.hero-title{position:absolute;left:180px;top:250px;color:var(--white)}
.hero-title h1{font-size:60px;font-weight:800;line-height:58px;letter-spacing:1px}
.hero-title p{font-size:12px;letter-spacing:2px;margin-top:8px;font-weight:500}
.bracket{position:absolute;width:40px;height:40px;border-color:var(--white);border-style:solid}
.bracket.tl{left:165px;top:232px;border-width:5px 0 0 5px}
.bracket.br{left:470px;top:345px;border-width:0 5px 5px 0}
.btn-start{position:absolute;left:228px;top:430px;width:96px;height:34px;background:var(--btn);color:var(--white);font-size:12px;display:flex;align-items:center;justify-content:center}

/* split sections */
.split{height:320px;background:var(--black);color:var(--white)}
.split .text{position:absolute;width:520px;top:60px}
.split h2{font-size:20px;font-weight:700;margin-bottom:14px}
.split p{font-size:13px;line-height:20px;color:var(--light-text)}
.split .more{margin-top:18px;font-size:13px;font-weight:600;display:flex;align-items:center;gap:8px;color:var(--white)}
.sell{top:560px}
.sell .text{left:30px}
.sell .photo{left:600px;top:0;width:600px;height:320px;background:linear-gradient(180deg,#20262a 0%,#2e3a40 55%,#6a4a2e 100%)}
.buy{top:870px}
.buy .text{left:630px;top:90px}
.buy .photo{left:0;top:0;width:600px;height:320px;background:linear-gradient(90deg,#9aa0a6 0%,#d8dadc 50%,#b4b8bc 100%)}

/* listings */
.listings{top:1330px;height:320px;background:var(--black);color:var(--white)}
.listings h2{text-align:center;font-size:18px;font-weight:700;margin-top:55px}
.strip{position:absolute;left:0;top:105px;width:1000px;height:205px;display:flex}
.strip .photo{position:relative;flex:1}
.p1{background:linear-gradient(180deg,#7fa0c0,#8a5a44 60%,#4e6a3a)}
.p2{background:linear-gradient(180deg,#9fb6cc,#e0e0dc 55%,#5f7a45)}
.p3{background:linear-gradient(180deg,#b8c6d4,#7a3e30 55%,#6a7a50)}
.p4{background:linear-gradient(180deg,#a8bcd0,#8c5e4a 55%,#4f6a3e)}
.arrow{position:absolute;top:195px;width:30px;height:30px}
.card{position:absolute;left:1000px;top:80px;width:200px;height:230px;background:var(--white);color:var(--ink);padding:14px 14px}
.card h3{font-size:16px;font-weight:700;color:var(--ink)}
.card .tag{font-size:9px;font-weight:700;color:var(--accent);margin:4px 0 10px;line-height:13px}
.card ul{list-style:none;font-size:10px;line-height:16px;color:var(--grey-text)}
.card ul li::before{content:"• "}
.card .label{font-size:9px;margin-top:12px;color:var(--grey-text)}
.card .price{font-size:17px;font-weight:700;color:var(--accent)}

/* info */
.info{top:1680px;height:260px;text-align:center}
.info h2{font-size:18px;font-weight:600;margin-top:40px;color:var(--ink)}
.info p{font-size:12px;line-height:18px;color:var(--grey-text);width:560px;margin:12px auto 0}
.info .buttons{display:flex;justify-content:center;gap:22px;margin-top:32px}
.info .buttons span{border:1px solid var(--ink);font-size:11px;font-weight:600;padding:10px 22px;letter-spacing:1px}

/* about */
.about{top:1980px;height:640px;color:var(--white)}
.about .bg{inset:0;background:linear-gradient(180deg,#0b0d12 0%,#15171c 45%,#2a2018 75%,#0c0c10 100%)}
.about .text{position:absolute;left:150px;top:95px;width:340px}
.about h2{font-size:18px;font-weight:700;margin-bottom:16px}
.about p{font-size:12px;line-height:18px;color:var(--light-text)}
.contact{margin-top:30px;font-size:12px;line-height:22px}
.contact strong{font-weight:700}
.contact .row{display:flex;align-items:center;gap:8px}
.about .portrait{left:800px;top:270px;width:340px;height:370px;background:linear-gradient(180deg,#3a3a3e 0%,#1e2026 100%)}

/* services */
.services{top:2620px;height:360px;display:flex;padding-left:148px;gap:70px}
.service{width:250px;margin-top:55px}
.service h3{font-size:14px;font-weight:700;color:var(--ink)}
.service .sub{font-size:9px;color:var(--grey-text);margin:3px 0 12px;font-style:normal}
.service p{font-size:11px;line-height:17px;color:var(--grey-text)}
.service .more{margin-top:16px;font-size:11px;font-weight:600;display:flex;align-items:center;gap:6px}

/* footer */
.footer{top:2980px;height:84px;background:var(--black);color:var(--white);display:flex;align-items:center;justify-content:space-between;padding:0 40px;font-size:11px}
.footer ul{display:flex;gap:18px;list-style:none;font-weight:600}
</style>
</head>
<body>

<header class="hero">
  <div class="photo" role="img" aria-label="Dunkles, modern eingerichtetes Wohnzimmer mit Fenster"></div>
  <nav class="nav">
    <div class="brand"><span class="brand-mark"></span>Wolde Immobilien</div>
    <ul class="menu"><li>Startseite</li><li>Verkaufen</li><li>Immobilien</li><li>Infos</li><li>Service</li><li>Partner</li><li>Kontakt</li></ul>
  </nav>
  <span class="bracket tl"></span><span class="bracket br"></span>
  <div class="hero-title">
    <h1>WOLDE REAL<br>ESTATE</h1>
    <p>YOUR MARKETER IN THE NORTH</p>
  </div>
  <div class="btn-start">Get Started</div>
</header>

<section class="split sell">
  <div class="text">
    <h2>IMMOBILIE VERKAUFEN</h2>
    <p>Wir verkaufen Ihre Immobilie zum bestmöglichen Preis. Kontaktieren Sie uns gern für eine kostenlose Marktwertermittlung und einen unverbindlichen Beratungstermin. Lesen Sie hier weiter, um zu sehen, wie Ihre Immobilie zu uns passt.</p>
    <div class="more"><svg width="12" height="10" viewBox="0 0 12 10"><path d="M0 5h10M6 1l4 4-4 4" stroke="#fff" stroke-width="1.6" fill="none"/></svg>Informationen zum Immobilienverkauf</div>
  </div>
  <div class="photo" role="img" aria-label="Blauer Sessel in einem Raum mit Holzboden"></div>
</section>

<section class="split buy">
  <div class="photo" role="img" aria-label="Helle Haustür in einem weißen Flur"></div>
  <div class="text">
    <h2>IMMOBILIE KAUFEN</h2>
    <p>Schauen Sie in unserem Immobilienportfolio vorbei und erfüllen Sie sich Ihren Traum vom Eigenheim. Sollte nicht das passende Objekt dabei sein, besuchen Sie unseren Service-Bereich für weitere Informationen.</p>
    <div class="more"><svg width="12" height="10" viewBox="0 0 12 10"><path d="M0 5h10M6 1l4 4-4 4" stroke="#fff" stroke-width="1.6" fill="none"/></svg>Informationen zum Immobilienkauf</div>
  </div>
</section>

<section class="listings">
  <h2>IMMOBILIEN</h2>
  <div class="strip">
    <div class="photo p1" role="img" aria-label="Rotes Backstein-Mehrfamilienhaus"></div>
    <div class="photo p2" role="img" aria-label="Weißes Einfamilienhaus mit Garten"></div>
    <div class="photo p3" role="img" aria-label="Altbau mit rotem Klinker"></div>
    <div class="photo p4" role="img" aria-label="Einfamilienhaus mit Rasenfläche"></div>
  </div>
  <svg class="arrow" style="left:10px" viewBox="0 0 30 30"><path d="M19 6l-9 9 9 9" stroke="#fff" stroke-width="3" fill="none"/></svg>
  <svg class="arrow" style="left:960px" viewBox="0 0 30 30"><path d="M11 6l9 9-9 9" stroke="#fff" stroke-width="3" fill="none"/></svg>
  <div class="card">
    <h3>WOHNUNG</h3>
    <div class="tag">GEEIGNET ZUR SELBSTNUTZUNG UND KAPITALANLAGE</div>
    <ul><li>ca. 47 m² Wohnfläche</li><li>Balkon</li><li>Modernes Badezimmer</li></ul>
    <div class="label">Kaufpreis</div>
    <div class="price">89.000,00 €</div>
  </div>
</section>

<section class="info">
  <h2>WICHTIGE INFORMATIONEN FÜR KÄUFER UND VERKÄUFER</h2>
  <p>Wir haben für Sie wichtige Informationen im Umgang mit Immobilien zusammengestellt. Wenn Sie Verkauf oder Kauf planen, finden Sie hier erste Hilfen.</p>
  <div class="buttons"><span>VERKÄUFER</span><span>KÄUFER</span></div>
</section>

<section class="about">
  <div class="photo bg" role="img" aria-label="Hafenstadt bei Nacht mit beleuchteter Kirche"></div>
  <div class="text">
    <h2>ÜBER WOLDE IMMOBILIEN</h2>
    <p>Wolde Immobilien hat sich auf den Verkauf und die Vermittlung privater Wohnimmobilien im Norden spezialisiert. Transparente Leistungen, individuelle Vermarktungsstrategien und die Nutzung moderner Vermarktungssysteme stehen für uns im Mittelpunkt.</p>
    <div class="contact">
      <strong>Lars Heinemann</strong><br>
      Immobilienmakler und Inhaber<br><br>
      <div class="row"><svg width="12" height="12" viewBox="0 0 12 12"><path d="M3 1l2 3-1.5 1.5a7 7 0 003 3L8 7l3 2-1.5 2C5 11 1 7 1 2.5z" fill="#fff"/></svg>+49 170 5550 128</div>
      <div class="row"><svg width="12" height="12" viewBox="0 0 12 12"><path d="M3 1l2 3-1.5 1.5a7 7 0 003 3L8 7l3 2-1.5 2C5 11 1 7 1 2.5z" fill="#fff"/></svg>+49 4101 555 40 20</div>
      <div class="row"><svg width="12" height="12" viewBox="0 0 12 12"><rect x="1" y="2.5" width="10" height="7" fill="none" stroke="#fff"/><path d="M1 2.5l5 4 5-4" stroke="#fff" fill="none"/></svg>anfrage@wolde-immobilien.de</div>
    </div>
  </div>
  <div class="photo portrait" role="img" aria-label="Porträt des Inhabers im Anzug"></div>
</section>

<section class="services">
  <div class="service">
    <h3>3D-BESICHTIGUNGEN</h3>
    <div class="sub">Innovative 3D-Rundgänge</div>
    <p>Als moderner Immobilienmakler bieten wir unseren Kunden virtuelle 3D-Besichtigungen an. Interessenten können das Objekt bequem von zu Hause erkunden und sich so einen realistischen Eindruck verschaffen.</p>
    <div class="more"><svg width="10" height="8" viewBox="0 0 12 10"><path d="M0 5h10M6 1l4 4-4 4" stroke="#111" stroke-width="1.6" fill="none"/></svg>Informationen zur 3D-Besichtigung</div>
  </div>
  <div class="service">
    <h3>FINANZIERUNG</h3>
    <div class="sub">Was sich leisten lässt</div>
    <p>Durch unsere Partner finden wir für Sie die passende Finanzierung. Gemeinsam prüfen wir Ihre Möglichkeiten und zeigen Ihnen, welche Immobilie zu Ihrem Budget passt und wie Sie sie sicher finanzieren.</p>
    <div class="more"><svg width="10" height="8" viewBox="0 0 12 10"><path d="M0 5h10M6 1l4 4-4 4" stroke="#111" stroke-width="1.6" fill="none"/></svg>Wissenswertes über die Finanzierung</div>
  </div>
  <div class="service">
    <h3>IMMOCHECK &amp; KAUFGUTACHTEN</h3>
    <div class="sub">Was ist meine Immobilie wert</div>
    <p>Wir bewerten Ihre Immobilie fundiert und erstellen auf Wunsch ein Kaufgutachten. So erhalten Sie eine verlässliche Grundlage für Ihre Entscheidung und den realistischen Wert Ihres Objektes.</p>
    <div class="more"><svg width="10" height="8" viewBox="0 0 12 10"><path d="M0 5h10M6 1l4 4-4 4" stroke="#111" stroke-width="1.6" fill="none"/></svg>Ablauf Immocheck</div>
  </div>
</section>

<footer class="footer">
  <span>© 2018 Wolde Immobilien</span>
  <ul><li>AGB</li><li>IMPRESSUM</li><li>DATENSCHUTZERKLÄRUNG</li><li>SITEMAP</li></ul>
</footer>

</body>
</html>
```